Physical Therapy Center for children Business Card

We need a Business Card for our company (Physical Therapy for children and youth with special needs) in Lisbon, Portugal. The name of the company is "Ninho de Luz"

The card must contain the following info:
- Logo: see uploaded file
- Name: Ninho de Luz
- Slogan: Cuidamos com carinho, crescemos juntos, celebramos conquistas!
- Service: Terapias Especializadas
- Address: Rua Henrique Lobato Farinha 9C
- ZipCode: 2741-318 Quinta do Vale Alto
- E-mail: geral@velado.pt
- Site: www.velado.pt
- Facebook: www.facebook.com/ninhodeluz
- Phone: +351 21 584 62 07
- Cell Phone: +351 96 731 84 25

The stationary should have contain all info from business card.

Target Market(s)

Parents of children with special needs

Industry/Entity Type

Physical Therapy

Contact Information for Business Card

The card design should be compatible with http://www.quellprensa.com/product2/order_detail.php?gid=40

Requirements
Should not have
• The business card should not have a Black background. Use white or other color.

```html
<!DOCTYPE html>
<html lang="pt">
<head>
<meta charset="utf-8">
<title>Ninho de Luz – Cartão de Visita</title>
<link rel="stylesheet" href="https://fonts.googleapis.com/css2?family=PT+Sans:wght@400;700&family=Source+Sans+3:wght@300;400&display=swap">
<style>
  :root {
    --backdrop: #d8d5d1;
    --card: #eceae7;
    --ink: #4d4c4b;
    --ink-soft: #5a5959;
    --teal: #21958a;
    --green: #1f9a80;
    --orange: #e5a223;
    --red: #c8302c;
    --purple: #6a2848;
    --wave: #4b4a4a;
    --on-wave: #ebebea;
    --on-wave-soft: #c9c8c6;
  }
  * { margin: 0; padding: 0; box-sizing: border-box; }
  html, body {
    width: 1200px; height: 969px; overflow: hidden;
    background: var(--backdrop);
  }
  .card {
    position: absolute; left: 100px; top: 201px;
    width: 1000px; height: 566px;
    background: var(--card);
    border-radius: 32px;
    overflow: hidden;
    box-shadow: 0 10px 30px rgba(0,0,0,0.15);
    font-family: "Source Sans 3", "Helvetica Neue", Arial, sans-serif;
  }
  .card-wave { position: absolute; inset: 0; }
  .brand-dot {
    position: absolute; left: 62px; top: 62px;
    width: 100px; height: 100px; border-radius: 50%;
    background: var(--teal);
  }
  .brand-name {
    position: absolute; left: 190px; top: 88px;
    font-family: "PT Sans", Arial, sans-serif;
    font-weight: 700; font-size: 60px; line-height: 1;
    color: var(--ink); letter-spacing: -0.5px;
  }
  .brand-slogan {
    position: absolute; left: 192px; top: 160px;
    font-family: "PT Sans", Arial, sans-serif;
    font-weight: 700; font-size: 16px; color: var(--ink);
    white-space: nowrap;
  }
  .person-name {
    position: absolute; left: 176px; top: 270px;
    font-family: "PT Sans", Arial, sans-serif;
    font-weight: 700; font-size: 38px; color: var(--ink-soft);
  }
  .person-role {
    position: absolute; left: 178px; top: 318px;
    font-family: "PT Sans", Arial, sans-serif;
    font-size: 27px; color: var(--teal);
  }
  .contacts {
    position: absolute; right: 40px; top: 254px;
    list-style: none; text-align: right;
  }
  .contacts li {
    display: flex; justify-content: flex-end; align-items: center;
    gap: 16px; height: 37.5px;
    font-size: 24px; font-weight: 300; color: var(--on-wave);
  }
  .contacts svg { width: 24px; height: 24px; fill: var(--on-wave); flex: none; }
  .address {
    position: absolute; right: 48px; top: 458px;
    text-align: right; font-size: 25px; font-weight: 300;
    line-height: 36px; color: var(--on-wave-soft);
  }
</style>
</head>
<body>
<div class="card">
  <svg class="card-wave" viewBox="0 0 1000 566" aria-hidden="true">
    <path d="M0,402 C120,500 260,530 420,440 S800,170 1000,120 L1000,566 L0,566 Z" fill="var(--wave)"/>
    <g transform="translate(0,-9)" fill="none" stroke-linecap="butt">
      <path d="M0,402 C120,500 260,530 420,440 S800,170 1000,120" pathLength="100" stroke="var(--green)" stroke-width="11" stroke-dasharray="0 0 21 100"/>
      <path d="M0,402 C120,500 260,530 420,440 S800,170 1000,120" pathLength="100" stroke="var(--orange)" stroke-width="11" stroke-dasharray="0 23 20 100"/>
      <path d="M0,402 C120,500 260,530 420,440 S800,170 1000,120" pathLength="100" stroke="var(--red)" stroke-width="9" stroke-dasharray="0 45 20 100"/>
      <path d="M0,402 C120,500 260,530 420,440 S800,170 1000,120" pathLength="100" stroke="var(--purple)" stroke-width="5" stroke-dasharray="0 67 33 100"/>
    </g>
  </svg>

  <div class="brand-dot"></div>
  <div class="brand-name">Ninho de Luz</div>
  <div class="brand-slogan">Cuidamos com carinho, crescemos juntos, celebramos conquistas</div>

  <div class="person-name">RUI MATOS</div>
  <div class="person-role">CEO/Founder</div>

  <ul class="contacts">
    <li>+351 21 584 62 07
      <svg viewBox="0 0 24 24"><path d="M6.6 10.8a15.1 15.1 0 0 0 6.6 6.6l2.2-2.2c.3-.3.7-.4 1-.2 1.1.4 2.3.6 3.6.6.6 0 1 .4 1 1V20c0 .6-.4 1-1 1A17 17 0 0 1 3 4c0-.6.4-1 1-1h3.5c.6 0 1 .4 1 1 0 1.2.2 2.4.6 3.6.1.3 0 .7-.2 1z"/></svg></li>
    <li>+351 96 731 84 25
      <svg viewBox="0 0 24 24"><path d="M7 1h10a2 2 0 0 1 2 2v18a2 2 0 0 1-2 2H7a2 2 0 0 1-2-2V3a2 2 0 0 1 2-2zm0 3v14h10V4zm5 15.5a1.2 1.2 0 1 0 0 2.4 1.2 1.2 0 0 0 0-2.4z"/></svg></li>
    <li>geral@velado.pt
      <svg viewBox="0 0 24 24"><path d="M2 5h20v14H2zm2 2v.4l8 5.2 8-5.2V7zm0 2.8V17h16V9.8l-8 5.2z"/></svg></li>
    <li>www.velado.pt
      <svg viewBox="0 0 24 24"><path d="M12 2a10 10 0 1 0 0 20 10 10 0 0 0 0-20zm-1 17.9A8 8 0 0 1 4.1 11L9 16v1a2 2 0 0 0 2 2zm6.9-2.5A2 2 0 0 0 16 16h-1v-3a1 1 0 0 0-1-1H8v-2h2a1 1 0 0 0 1-1V7h2a2 2 0 0 0 2-2v-.4a8 8 0 0 1 2.9 12.8z"/></svg></li>
    <li>ninhodeluz
      <svg viewBox="0 0 24 24"><rect x="2" y="2" width="20" height="20" rx="2"/></svg></li>
  </ul>

  <div class="address">
    Rua Henrique Lobato Farinha 9C<br>
    ZipCode: 2741-318 Quinta do Vale Alto
  </div>
</div>
</body>
</html>
```